Business card for Chiropractic clinics needs reworked / redesigned

The business card in attachment was designed 10 years ago. It is in need of an update.
We have 2 clinics:
VELDHOVE KLINIEK & VELDHOVE KLINIEK NOORD
Only one address needs to be on the card for doctors that only work in one clinic and two addresses need to be on the card for the doctors that work in both clinics.

Target Market(s)

patients/referrers

Industry/Entity Type

Medical

Contact Information for Business Card

Logo (in full or zoomed-in)
Clinic Name
Doctor name and title
clinic address, website, tel, email

Font styles to use
Sans Serif

Colors

Designer to choose colors to be used in the design.

Requirements
Must have
• Good contrast/readability
• We like modern minimalistic designs
• The Bcard needs to project our very high standard of proficiency/professionalism
Should not have
• Not curly
• Not to much colours

```html
<!DOCTYPE html>
<html lang="nl">
<head>
<meta charset="utf-8">
<title>Veldhove Kliniek – visitekaartje</title>
<link href="https://fonts.googleapis.com/css2?family=Roboto:wght@400;500;700&display=swap" rel="stylesheet">
<style>
  :root {
    --bg: #d9d9d9;
    --card: #f4f4f4;
    --ink: #0e2a2a;
    --text: #3a3a3a;
    --muted: #a6a6a6;
    --rule: #555;
  }
  * { margin: 0; padding: 0; box-sizing: border-box; }
  html, body { width: 1200px; height: 960px; overflow: hidden; }
  body { background: var(--bg); font-family: "Roboto", Arial, sans-serif; position: relative; }

  .card { position: absolute; width: 600px; height: 343px; background: var(--card); border: 1px solid #cfcfcf; }
  .card--front { left: 314px; top: 113px; }
  .card--back { left: 311px; top: 472px; }

  .doctor { position: absolute; top: 56px; left: 0; width: 100%; text-align: center; }
  .doctor__name { font-size: 21px; font-weight: 700; color: var(--ink); letter-spacing: 0.2px; line-height: 24px; }
  .doctor__title { font-size: 14px; color: var(--muted); letter-spacing: 0.6px; line-height: 18px; }
  .doctor__number { font-size: 18px; font-weight: 700; color: var(--ink); line-height: 26px; margin-top: 1px; }

  .divider { position: absolute; top: 145px; left: 38px; width: 524px; height: 1px; background: var(--rule); }
  .divider__accent { position: absolute; left: 191px; top: -2px; width: 142px; height: 5px; background: var(--ink); }

  .clinic { position: absolute; top: 212px; font-size: 14px; color: var(--text); line-height: 19px; }
  .clinic--main { left: 37px; }
  .clinic--north { right: 38px; text-align: right; }
  .clinic__name { font-weight: 700; color: #4a4a4a; }
  .clinic__contacts { list-style: none; margin-top: 5px; }
  .clinic__contacts li { display: flex; align-items: center; gap: 7px; }
  .clinic--north .clinic__contacts li { justify-content: flex-end; }
  .icon { width: 13px; height: 13px; fill: var(--ink); flex: none; }

  .brand { position: absolute; top: 140px; left: 0; width: 100%; display: flex; justify-content: center; align-items: center; gap: 12px; }
  .brand__dot { width: 14px; height: 14px; border-radius: 50%; background: var(--ink); }
  .brand__name { font-size: 24px; font-weight: 500; color: var(--ink); letter-spacing: 2px; }
  .back__web { position: absolute; top: 290px; left: 0; width: 100%; text-align: center; font-size: 15px; color: var(--text); letter-spacing: 3px; }
</style>
</head>
<body>
  <section class="card card--front">
    <header class="doctor">
      <h1 class="doctor__name">MAARTEN VERLINDE D.C.</h1>
      <p class="doctor__title">CHIROPRACTOR</p>
      <p class="doctor__number">0.47215.38.000</p>
    </header>
    <div class="divider"><span class="divider__accent"></span></div>

    <div class="clinic clinic--main">
      <p class="clinic__name">Veldhove Kliniek</p>
      <p>Kastanjelaan 41, 9000 Gent</p>
      <ul class="clinic__contacts">
        <li><svg class="icon" viewBox="0 0 16 16"><path d="M3.5 1l2.5 3-1.5 2c1 2 3 4 5 5l2-1.5 3 2.5-1.5 2.5C7 14 2 9 1 2.5z"/></svg>+32 (0)9 000.41.26</li>
        <li><svg class="icon" viewBox="0 0 16 16"><path d="M1 3h14v10H1z M1 3l7 6 7-6" fill="var(--ink)" stroke="#f4f4f4" stroke-width="1.2"/></svg>info@veldhovekliniek.be</li>
        <li><svg class="icon" viewBox="0 0 16 16"><circle cx="8" cy="8" r="7"/><path d="M8 1c-2 2-2 12 0 14M8 1c2 2 2 12 0 14M1 8h14" stroke="#f4f4f4" stroke-width="1" fill="none"/></svg>www.veldhovekliniek.be</li>
      </ul>
    </div>

    <div class="clinic clinic--north">
      <p class="clinic__name">Veldhove Kliniek Noord</p>
      <p>Molenstraat 27</p>
      <ul class="clinic__contacts">
        <li>+32 (0)9 000.58.39<svg class="icon" viewBox="0 0 16 16"><path d="M3.5 1l2.5 3-1.5 2c1 2 3 4 5 5l2-1.5 3 2.5-1.5 2.5C7 14 2 9 1 2.5z"/></svg></li>
        <li>info@veldhovenoord.be<svg class="icon" viewBox="0 0 16 16"><path d="M1 3h14v10H1z M1 3l7 6 7-6" fill="var(--ink)" stroke="#f4f4f4" stroke-width="1.2"/></svg></li>
        <li>www.veldhovenoord.be<svg class="icon" viewBox="0 0 16 16"><circle cx="8" cy="8" r="7"/><path d="M8 1c-2 2-2 12 0 14M8 1c2 2 2 12 0 14M1 8h14" stroke="#f4f4f4" stroke-width="1" fill="none"/></svg></li>
      </ul>
    </div>
  </section>

  <section class="card card--back">
    <div class="brand">
      <span class="brand__dot"></span>
      <span class="brand__name">VELDHOVE KLINIEK</span>
    </div>
    <p class="back__web">www.veldhovekliniek.be</p>
  </section>
</body>
</html>
```